Criação de Folheto ou Cartaz (sem dobra) para Contabilidade & Finanças
A empresa queria:
" PRESTADORA DE SERVIÇOS PARA EMPRESAS DO SIMPLES, LUCRO PRESUMIDO, L REAL, MEI, E-SOCIAL, PROCESSOS ADMINISTRATIVOS FISCAIS E TRIBUTARIOS, AUDITORIA ASSESSORIA E CONSULTORIA CONTABIL, NAS AREAS CONTABEIS, FISCAIS, DEPARTAMENTO PESSOAL, LEGALIZAÇÃO E REGULARIZAÇÃO DE EMPRESAS. "

```html
<!DOCTYPE html>
<html lang="pt-BR">
<head>
<meta charset="utf-8">
<title>Norte Gestão Contábil e Tributária — Folheto</title>
<link rel="stylesheet" href="https://fonts.googleapis.com/css2?family=Oswald:wght@500;600&family=Open+Sans:wght@400;600;700&display=swap">
<style>
  :root{
    --red:#d7262c;
    --red-dark:#a8181d;
    --ink:#3a3a3a;
    --grey-dark:#5b5b5b;
    --grey-mid:#8a8a8a;
    --grey-light:#e9e9ea;
    --paper:#ffffff;
    --stage:#d2d2d2;
  }
  *{box-sizing:border-box;margin:0;padding:0}
  html,body{width:1200px;height:1200px;overflow:hidden}
  body{background:var(--stage);font-family:"Open Sans",Arial,sans-serif;color:var(--ink);position:relative}
  .flyer{position:absolute;left:200px;top:35px;width:800px;height:1130px;background:var(--paper);overflow:hidden}
  .hero-photo{position:absolute;left:0;top:0;width:800px;height:430px;
    background:linear-gradient(135deg,#c9ccd1 0%,#eef0f3 35%,#dfe6f0 60%,#8aa4c4 100%)}
  .swoosh{position:absolute;left:0;top:380px;width:800px;height:130px}
  .brand{position:absolute;left:40px;top:480px;display:flex;align-items:center;gap:14px}
  .brand-mark{width:26px;height:26px;background:var(--red)}
  .brand-name{font-family:"Oswald",sans-serif;font-weight:600;font-size:30px;color:var(--grey-dark);text-transform:uppercase;letter-spacing:.5px;line-height:1}
  .headline{position:absolute;left:62px;top:565px;padding-left:16px;border-left:5px solid var(--red);
    font-family:"Oswald",sans-serif;font-weight:500;font-size:38px;line-height:1.2;color:var(--grey-dark);text-transform:uppercase}
  .headline .accent{color:var(--red)}
  .intro{position:absolute;left:60px;right:40px;top:680px;font-size:25px;line-height:1.3;color:var(--ink);text-indent:22px}
  .section-band{position:absolute;left:0;top:808px;width:470px;height:48px}
  .section-title{position:absolute;left:42px;top:810px;font-family:"Oswald",sans-serif;font-weight:500;font-size:29px;color:#fff;letter-spacing:1px}
  .services{position:absolute;top:888px;list-style:none;font-family:"Oswald",sans-serif;font-weight:500;font-size:22px;color:var(--grey-dark);line-height:1.15}
  .services li{margin-bottom:14px}
  .services li::before{content:"- "}
  .services--left{left:50px}
  .services--right{left:405px}
  .services .cont{display:block;padding-left:14px}
  .footer-band{position:absolute;left:0;top:1015px;width:800px;height:115px}
  .contacts{position:absolute;left:28px;top:1050px;list-style:none;font-size:14px;color:#fff;line-height:1}
  .contacts li{display:flex;align-items:center;gap:8px;margin-bottom:9px}
  .contacts svg{width:16px;height:16px;flex:none}
  .address{position:absolute;left:430px;top:1055px;display:flex;gap:8px;font-size:13px;color:#fff;line-height:1.3}
  .address svg{width:18px;height:22px;flex:none;margin-top:2px}
</style>
</head>
<body>
<main class="flyer">
  <div class="hero-photo" role="img" aria-label="Fotografia de mesa de escritório com calculadora, relatórios financeiros com gráficos e notebook exibindo painel de metas"></div>

  <svg class="swoosh" viewBox="0 0 800 130" aria-hidden="true">
    <polygon points="0,60 800,0 800,40 0,110" fill="var(--grey-light)"/>
    <polygon points="0,40 520,0 800,0 0,70" fill="var(--red)"/>
    <polygon points="0,70 800,10 800,22 0,88" fill="var(--red-dark)" opacity=".35"/>
    <polygon points="0,95 800,35 800,130 0,130" fill="var(--paper)"/>
    <polygon points="560,130 800,70 800,84 620,130" fill="var(--grey-light)"/>
  </svg>

  <div class="brand">
    <span class="brand-mark"></span>
    <span class="brand-name">Norte Gestão Contábil e Tributária</span>
  </div>

  <h1 class="headline">Soluções em <span class="accent">serviços contábeis</span><br>especializados para sua empresa</h1>

  <p class="intro">Cuidamos de todos os processos contábeis da forma mais segura e com profissionais qualificados para entregar a melhor solução para sua empresa!</p>

  <svg class="section-band" viewBox="0 0 470 48" aria-hidden="true">
    <polygon points="0,0 440,0 470,48 0,48" fill="var(--red)"/>
  </svg>
  <h2 class="section-title">ESPECIALIDADES</h2>

  <ul class="services services--left">
    <li>IMPOSTOS DE RENDA PESSOA FÍSICA</li>
    <li>INVENTÁRIO PATRIMONIAL</li>
  </ul>
  <ul class="services services--right">
    <li>DEPARTAMENTO PESSOAL</li>
    <li>CONSTITUIÇÃO, ALTERAÇÕES<span class="cont">E BAIXAS DE EMPRESAS</span></li>
  </ul>

  <svg class="footer-band" viewBox="0 0 800 115" aria-hidden="true">
    <polygon points="0,30 800,0 800,115 0,115" fill="var(--grey-dark)"/>
    <polygon points="0,18 800,-12 800,0 0,30" fill="var(--red)"/>
  </svg>

  <ul class="contacts">
    <li><svg viewBox="0 0 24 24"><path fill="#fff" d="M6.6 10.8a15 15 0 0 0 6.6 6.6l2.2-2.2c.3-.3.7-.4 1-.2 1.1.4 2.3.6 3.6.6.6 0 1 .4 1 1V20c0 .6-.4 1-1 1A17 17 0 0 1 3 4c0-.6.4-1 1-1h3.5c.6 0 1 .4 1 1 0 1.3.2 2.5.6 3.6.1.3 0 .7-.2 1z"/></svg>(62) 3100-4821</li>
    <li><svg viewBox="0 0 24 24"><circle cx="12" cy="12" r="11" fill="#fff"/><path fill="var(--grey-dark)" d="M9 7.5c.3 0 .5.1.6.4l.8 1.8c.1.3 0 .6-.2.8l-.6.6a7 7 0 0 0 3.3 3.3l.6-.6c.2-.2.5-.3.8-.2l1.8.8c.3.1.4.3.4.6v1.2c0 .6-.5 1-1 1A8.5 8.5 0 0 1 7 8.5c0-.5.4-1 1-1z"/></svg>(62) 99800-2734</li>
    <li><svg viewBox="0 0 24 24"><rect x="2" y="5" width="20" height="14" rx="1.5" fill="#fff"/><path d="M3 6l9 7 9-7" fill="none" stroke="var(--grey-dark)" stroke-width="1.6"/></svg>contato@nortegestaocontabil.com.br</li>
  </ul>

  <div class="address">
    <svg viewBox="0 0 20 26"><path fill="#fff" d="M10 0a9 9 0 0 0-9 9c0 6.5 9 17 9 17s9-10.5 9-17a9 9 0 0 0-9-9zm0 12.5A3.5 3.5 0 1 1 10 5.5a3.5 3.5 0 0 1 0 7z"/></svg>
    <p>Av. das Palmeiras nº 410 sala 802 - Centro Aurora<br>Ed. Horizonte Setor Jardim Novo<br>(próximo à Praça Central) Goiânia/GO CEP: 74.000-100</p>
  </div>
</main>
</body>
</html>
```